Petrochemical Spool Pipe Manufacturer Needs a Brochure Design (Granite Ridge Fabricators, LLC.)

We need a two page folding brochure with all faces used that will have our Logo and representative pictures of refinery type piping systems. It will also need to have text block place holder where we can fill in our statements, capabilities and facility specifications. The cover needs to be outstanding with a combination of pictures and text. The file type provided needs to be Adobe Illustrator or Photoshop CC

Target Market(s)

Any large plant being built that will require a large quantity of piping to be manufactured. Upstream Oil and Gas (Refineries, Petrochemical, Paper, etc.)

Industry/Entity Type

Oil And Gas

Font styles to use
Other font styles liked:
• Times New Roman

Colors
ec1f27

Requirements
Must have
• A polished professional look (We are Engineers and CAD Designers who run the company) All Pages being utilized, A place for contact information easy eye contact, Matching Company colors
Nice to have
• A spot to hold a business card, Please notice two pictures of past projects attached along with our logo. ( Picture not intended to be included in design only to give a representative of projects completed and market)
Should not have
• Any kind of checker steel patterns professional corporation not dinky fab shop.

```html
<!DOCTYPE html>
<html lang="en">
<head>
<meta charset="utf-8">
<title>Granite Ridge Fabricators – Brochure</title>
<link href="https://fonts.googleapis.com/css2?family=Lato:wght@400;700;900&family=Michroma&display=swap" rel="stylesheet">
<style>
  :root {
    --red: #ec1f27;
    --red-deep: #c8141b;
    --charcoal: #2a2a2d;
    --charcoal-dark: #1c1c1e;
    --white: #ffffff;
    --paper: #f4f4f4;
    --ink: #333335;
    --steel-light: #c9d6e3;
    --steel-dark: #4d6278;
    --bg: #e9e9e9;
  }
  * { box-sizing: border-box; margin: 0; padding: 0; }
  html, body { width: 1200px; height: 1200px; overflow: hidden; background: var(--bg); }
  body { position: relative; font-family: "Lato", sans-serif; }

  .spread { position: absolute; left: 200px; width: 800px; height: 540px; display: flex; box-shadow: 0 10px 30px rgba(0,0,0,.18); }
  .spread--outside { top: 30px; }
  .spread--inside { top: 630px; }

  .page { position: relative; width: 400px; height: 540px; overflow: hidden; }
  .page__shapes { position: absolute; inset: 0; width: 400px; height: 540px; }

  .brand { position: absolute; display: flex; align-items: center; gap: 8px; }
  .brand__dot { width: 16px; height: 16px; border-radius: 50%; background: var(--red); flex: none; }
  .brand__name { font-family: "Lato", sans-serif; font-weight: 900; font-size: 15px; line-height: 1.05; color: var(--red); text-transform: uppercase; letter-spacing: .5px; }
  .brand--on-dark .brand__name { color: var(--white); }

  .url { position: absolute; width: 100%; text-align: center; font-size: 10px; font-weight: 700; }

  .pill { display: inline-block; background: var(--red); color: var(--white); font-weight: 700; font-size: 11px; border-radius: 12px; padding: 4px 14px; }

  /* back cover */
  .back-cover .brand { left: 120px; top: 225px; }
  .contact-box { position: absolute; left: 105px; top: 285px; width: 190px; height: 95px; border: 2px solid #8a8a8d; border-radius: 16px; text-align: center; color: var(--white); padding-top: 14px; font-size: 10.5px; font-weight: 700; line-height: 1.35; }
  .contact-box .pill { margin-top: 6px; }
  .back-cover .url { top: 506px; color: var(--red); }

  /* front cover */
  .front-cover .brand { left: 150px; top: 42px; }
  .cta-circle { position: absolute; left: 30px; top: 268px; width: 156px; height: 156px; border-radius: 50%; background: var(--white); border: 6px solid var(--red); display: flex; flex-direction: column; justify-content: center; align-items: center; font-family: "Michroma", sans-serif; font-size: 10.5px; line-height: 1.5; text-align: center; }
  .cta-circle .accent { color: var(--red); }
  .cta-circle .plain { color: var(--ink); }
  .headline { position: absolute; left: 200px; top: 290px; width: 195px; font-family: "Michroma", sans-serif; font-size: 16.5px; line-height: 1.45; color: var(--white); }
  .headline .accent { color: var(--red); display: block; }
  .headline .plain { display: block; }
  .front-cover .url { top: 500px; color: var(--white); }

  /* overview page */
  .overview__title { position: absolute; left: 30px; top: 240px; font-size: 15px; color: var(--red); letter-spacing: 1px; font-weight: 400; }
  .overview__body { position: absolute; left: 30px; top: 266px; width: 340px; color: var(--white); font-size: 9.6px; line-height: 1.38; }
  .overview__body p + p { margin-top: 7px; }
  .overview .url { top: 506px; color: var(--white); }

  /* company page */
  .company__body { position: absolute; left: 30px; top: 34px; width: 340px; color: var(--ink); font-size: 8.6px; line-height: 1.4; }
  .company__body p + p { margin-top: 8px; }
  .card-slot { position: absolute; left: 50px; top: 282px; width: 270px; height: 96px; border: 3px solid var(--red); border-radius: 16px; background: var(--white); display: flex; align-items: center; justify-content: center; font-size: 14px; font-weight: 700; color: var(--ink); letter-spacing: .5px; }
  .company .brand { left: 30px; top: 410px; }
  .company .pill { position: absolute; right: 30px; top: 420px; }
  .company .url { top: 510px; color: var(--ink); }
</style>
</head>
<body>

<!-- OUTSIDE SPREAD -->
<section class="spread spread--outside">

  <article class="page back-cover">
    <svg class="page__shapes" viewBox="0 0 400 540" aria-hidden="false">
      <defs>
        <linearGradient id="steelPipes" x1="0" y1="0" x2="1" y2="1">
          <stop offset="0" stop-color="#e4edf5"/>
          <stop offset=".5" stop-color="#8ea5bb"/>
          <stop offset="1" stop-color="#34475c"/>
        </linearGradient>
      </defs>
      <rect width="400" height="540" fill="var(--charcoal)"/>
      <path d="M0 0 H400 V70 C300 205 120 200 0 110 Z" fill="url(#steelPipes)" role="img" aria-label="Photo of stainless steel refinery piping"/>
      <path d="M0 110 C120 200 300 205 400 70" fill="none" stroke="var(--red)" stroke-width="5"/>
      <path d="M0 405 C130 470 290 480 400 455 V540 H0 Z" fill="var(--white)"/>
      <path d="M0 405 C130 470 290 480 400 455" fill="none" stroke="var(--red)" stroke-width="4"/>
    </svg>
    <div class="brand brand--on-dark"><span class="brand__dot"></span><span class="brand__name">Granite Ridge<br>Fabricators</span></div>
    <div class="contact-box">
      2290 Harbor Mill Rd<br>Port Alden, LA 70999<br>
      <span class="pill">Phone: 555.014.2290</span>
    </div>
    <div class="url">www.graniteridge-fab.com</div>
  </article>

  <article class="page front-cover">
    <svg class="page__shapes" viewBox="0 0 400 540">
      <defs>
        <linearGradient id="workerScene" x1="0" y1="0" x2="1" y2="0">
          <stop offset="0" stop-color="#2d5fa8"/>
          <stop offset=".55" stop-color="#b9c6d3"/>
          <stop offset="1" stop-color="#5a6a7c"/>
        </linearGradient>
      </defs>
      <rect width="400" height="540" fill="var(--white)"/>
      <path d="M0 150 C110 95 290 90 400 150 V300 H0 Z" fill="url(#workerScene)" role="img" aria-label="Photo of a technician in a hard hat working on process piping"/>
      <path d="M0 150 C110 95 290 90 400 150" fill="none" stroke="var(--red)" stroke-width="5"/>
      <path d="M0 330 C140 290 290 270 400 265 V540 H0 Z" fill="var(--charcoal)"/>
      <path d="M0 330 C140 290 290 270 400 265" fill="none" stroke="var(--red)" stroke-width="4"/>
      <path d="M0 470 C150 430 300 420 400 400 V540 H0 Z" fill="var(--red)"/>
      <path d="M0 470 C150 430 300 420 400 400" fill="none" stroke="var(--white)" stroke-width="5"/>
    </svg>
    <div class="brand"><span class="brand__dot"></span><span class="brand__name">Granite Ridge<br>Fabricators</span></div>
    <div class="cta-circle">
      <span class="accent">CONTACT US</span>
      <span class="plain">FOR YOUR</span>
      <span class="accent">NEXT PROJECT!</span>
    </div>
    <h1 class="headline">
      <span class="plain">WE HAVE</span>
      <span class="accent">THE RIGHT</span>
      <span class="plain">EXPERIENCE</span>
      <span class="accent">RIGHT NOW!</span>
    </h1>
    <div class="url">www.graniteridge-fab.com</div>
  </article>
</section>

<!-- INSIDE SPREAD -->
<section class="spread spread--inside">

  <article class="page overview">
    <svg class="page__shapes" viewBox="0 0 400 540">
      <defs>
        <linearGradient id="copperPipes" x1="0" y1="0" x2="1" y2="1">
          <stop offset="0" stop-color="#c97a4a"/>
          <stop offset="1" stop-color="#8d99a6"/>
        </linearGradient>
        <linearGradient id="towers" x1="0" y1="0" x2="0" y2="1">
          <stop offset="0" stop-color="#6aa2d6"/>
          <stop offset="1" stop-color="#b8c2cc"/>
        </linearGradient>
      </defs>
      <rect width="400" height="540" fill="var(--charcoal)"/>
      <path d="M0 0 H400 V175 C330 105 200 85 0 125 Z" fill="var(--red)"/>
      <path d="M0 460 C150 420 300 470 400 500 V540 H0 Z" fill="var(--red)"/>
      <circle cx="85" cy="105" r="64" fill="var(--white)"/>
      <circle cx="85" cy="105" r="58" fill="var(--red)"/>
      <circle cx="85" cy="105" r="54" fill="url(#copperPipes)" role="img" aria-label="Photo of copper and steel process piping"/>
      <circle cx="245" cy="150" r="72" fill="var(--white)"/>
      <circle cx="245" cy="150" r="66" fill="var(--red)"/>
      <circle cx="245" cy="150" r="62" fill="url(#towers)" role="img" aria-label="Photo of refinery distillation towers"/>
    </svg>
    <h2 class="overview__title">OVERVIEW</h2>
    <div class="overview__body">
      <p>Granite Ridge Fabricators (GRF) is dedicated to the customized design and manufacturing of engineered packages and modules for the oil and gas industry. We have earned an outstanding reputation for providing the highest quality oil and gas processing plants and equipment for a wide range of customers in the upstream, midstream and downstream markets. Numerous clients across the U.S. and internationally have come to rely upon GRF to deliver reliable, cost efficient products on time and within budget.</p>
      <p>GRF offers multiple state-of-the-art manufacturing facilities that are equipped with the latest in fabrication equipment and technology. We have the capabilities to handle virtually any size project including those that require heavy lifting. In addition, our team of talented and experienced engineers provides a wide range of engineering services utilizing the industry's most advanced software to design almost any package imaginable. Our team also includes a group of skilled manufacturing professionals who are dedicated to safely and efficiently fabricating products that meet the highest standards of quality.</p>
    </div>
    <div class="url">www.graniteridge-fab.com</div>
  </article>

  <article class="page company">
    <svg class="page__shapes" viewBox="0 0 400 540">
      <defs>
        <linearGradient id="plantFade" x1="0" y1="0" x2="0" y2="1">
          <stop offset="0" stop-color="#ffffff"/>
          <stop offset="1" stop-color="#dcdcdc"/>
        </linearGradient>
      </defs>
      <rect width="400" height="540" fill="var(--white)"/>
      <rect x="0" y="250" width="400" height="290" fill="url(#plantFade)" role="img" aria-label="Faded photo of a processing plant"/>
      <path d="M0 485 C120 455 290 445 400 470" fill="none" stroke="var(--red)" stroke-width="3"/>
    </svg>
    <div class="company__body">
      <p>Founded in 2010 and headquartered in Port Alden, Louisiana, GRF is led by a group of owners who each possess more than 20 years of experience in the design and manufacturing of process equipment. Since the founding of our company, we have grown from four employees to encompass a workforce of more than 200 professionals. In addition, we have grown from a handful of local clients to serving more than 30 respected oil and gas companies throughout the U.S. and beyond. In addition to our headquarters and manufacturing facilities, GRF also offers sales and service offices in Bogota, Colombia in order to better meet the needs of our customers in South America. GRF also has established strategic relationships in many parts of the globe to support our international sales.</p>
      <p>At GRF we also pride ourselves on providing superior customer service and attention to detail. We provide personalized attention and are dedicated to meeting each customer's unique needs while also helping to solve problems and increase the efficiency of their processing systems and equipment. We also strive to build long-term relationships with our customers – which is why our company receives a great deal of repeat business.</p>
    </div>
    <div class="card-slot">BUSINESS CARD</div>
    <div class="brand"><span class="brand__dot"></span><span class="brand__name">Granite Ridge<br>Fabricators</span></div>
    <span class="pill">Phone: 555.014.2290</span>
    <div class="url">www.graniteridge-fab.com</div>
  </article>
</section>

</body>
</html>
```